Label For Hand soap

Hello,

I would like to get your assistance with creating a label for my hand soap that I am in the process of developing. I would like the label to look simple visually appealing and eye catching similar to a cologne bottle's label. I would like there to be graphic or illustration accompanied with the text. The color scheme is black. I would like the background of the label to be transparent so that I can show the color of my product. I have attached some pictures of my bottle and some labels that I like for your reference. The name of my brand is Vrell. The hand soap scent is candied pineapples.

Thanks

```html
<!DOCTYPE html>
<html lang="en">
<head>
<meta charset="utf-8">
<title>Vrell Hand Soap Label</title>
<link href="https://fonts.googleapis.com/css2?family=Playfair+Display:wght@400;700&display=swap" rel="stylesheet">
<style>
  :root {
    --ink: #111111;
    --paper: #ffffff;
    --ornament: #c9c9c9;
    --pattern: #8c8c8c;
  }
  html, body {
    margin: 0;
    padding: 0;
    width: 993px;
    height: 1200px;
    overflow: hidden;
    background: var(--paper);
  }
  .label {
    position: relative;
    width: 993px;
    height: 1200px;
    background: var(--paper);
    font-family: "Playfair Display", Georgia, serif;
    color: var(--ink);
  }
  .label-art {
    position: absolute;
    inset: 0;
  }
  .brand-name {
    position: absolute;
    top: 112px;
    left: 0;
    width: 100%;
    text-align: center;
    font-size: 112px;
    font-weight: 400;
    line-height: 1;
    margin: 0;
  }
  .product-title {
    position: absolute;
    top: 432px;
    left: 0;
    width: 100%;
    text-align: center;
    margin: 0;
    font-size: 182px;
    font-weight: 400;
    line-height: 174px;
    letter-spacing: -2px;
  }
  .scent-name {
    position: absolute;
    top: 918px;
    left: 0;
    width: 100%;
    text-align: center;
    margin: 0;
    font-size: 31px;
    font-weight: 700;
    line-height: 1;
    color: var(--paper);
  }
  .volume {
    position: absolute;
    top: 1086px;
    left: 0;
    width: 100%;
    text-align: center;
    margin: 0;
    font-size: 42px;
    font-variant: small-caps;
    line-height: 1;
  }
</style>
</head>
<body>
<main class="label">
  <svg class="label-art" width="993" height="1200" viewBox="0 0 993 1200" xmlns="http://www.w3.org/2000/svg">
    <!-- outer frame -->
    <rect x="6" y="6" width="981" height="1188" fill="none" stroke="var(--ink)" stroke-width="4"/>
    <path role="img" aria-label="Greek key border pattern" fill="var(--pattern)" fill-rule="evenodd"
          d="M12 12 H981 V1188 H12 Z M46 46 V1154 H947 V46 Z"/>
    <rect x="50" y="50" width="893" height="1100" fill="none" stroke="var(--ink)" stroke-width="3"/>

    <!-- corner flourishes -->
    <path role="img" aria-label="Scrolling leaf flourish, top left corner" fill="var(--ornament)"
          d="M60 60 H300 Q230 80 190 120 Q120 170 130 290 Q90 260 60 280 Z"/>
    <path role="img" aria-label="Scrolling leaf flourish, top right corner" fill="var(--ornament)"
          d="M933 60 H693 Q763 80 803 120 Q873 170 863 290 Q903 260 933 280 Z"/>
    <path role="img" aria-label="Scrolling leaf flourish, bottom left corner" fill="var(--ornament)"
          d="M60 1140 H300 Q230 1120 190 1080 Q120 1030 130 900 Q90 930 60 910 Z"/>
    <path role="img" aria-label="Scrolling leaf flourish, bottom right corner" fill="var(--ornament)"
          d="M933 1140 H693 Q763 1120 803 1080 Q873 1030 863 900 Q903 930 933 910 Z"/>

    <!-- title panel -->
    <rect x="158" y="384" width="677" height="426" rx="44" fill="none" stroke="var(--ink)" stroke-width="3"/>
    <path role="img" aria-label="Chain link pattern border" fill="var(--pattern)" fill-rule="evenodd"
          d="M206 390 H787 A38 38 0 0 1 829 428 V766 A38 38 0 0 1 787 804 H206 A38 38 0 0 1 164 766 V428 A38 38 0 0 1 206 390 Z
             M214 410 H779 A30 30 0 0 1 809 440 V754 A30 30 0 0 1 779 784 H214 A30 30 0 0 1 184 754 V440 A30 30 0 0 1 214 410 Z"/>
    <rect x="186" y="412" width="621" height="370" rx="28" fill="var(--paper)" stroke="var(--ink)" stroke-width="3"/>

    <!-- scent banner -->
    <polygon points="158,938 240,866 258,884 735,884 753,866 835,938 753,1010 735,992 258,992 240,1010"
             fill="var(--paper)" stroke="var(--ink)" stroke-width="4" stroke-linejoin="round"/>
    <polygon points="176,938 240,882 254,896 739,896 753,882 817,938 753,994 739,980 254,980 240,994"
             fill="none" stroke="var(--ink)" stroke-width="2" stroke-linejoin="round"/>
    <polygon points="252,938 292,906 701,906 741,938 701,970 292,970" fill="var(--ink)"/>
  </svg>

  <h1 class="brand-name">Vrell</h1>
  <h2 class="product-title">HAND<br>SOAP</h2>
  <p class="scent-name">CANDIED PINEAPPLES.</p>
  <p class="volume">8 fl.oz.</p>
</main>
</body>
</html>
```